Church needs a graphic design/flyer layout for upcoming series

I need a multi-purpose design for promoting both our upcoming series of messages and our fall kick-off event where we will launch the messages.

Our promotion will be printed on a two-sided. One side is simple and focuses on the series and the other side has details in regards to the event. I have provided an attachment example of what we did last time.

The design needs to be multi-purpose because it will be used for our sermon Power Points, placed on our website banner, social media, etc.

• Sermon series is called “Harbor Lanterns”
• The subtitle will be “What’s keeping you from God?”
• Our name logo should be on the graphic as well.
• The subject manner will revolve around common hurdles that people face about God and Christianity: The existence of God, the exclusivity of religion, Hell, the reliability of the Bible, Hypocrisy in the church, etc.
• Our mission is “Connecting Young Families to Christ” so our focus is to reach out to families while not being exclusive to others.
• Our target audience is families with school-aged kids.
• This series is an invitational focus so we want it to be appealing to non-church goers.
• It should be attention grabbing while not being too ‘edgy’

• The front of the card will most likely consist the Sermon Series Graphic, title & subtitle of the series, and perhaps our name logo somewhere on it.
• The back of the card will invite and give the basic information for the event so that the people will be encouraged to save the date and come to the event.
• Here are some things that could be included on that advertisement:
o The name of the event: “Westbrook Commons Open Day”
o The date and time of the event: Sept 23rd @ 10:30
o Features of the event:
 Free lunch
 Children’s program
 Bouncy Castle
 Start of the “Harbor Lanterns” messages.
 Sample of topics
o Information about the church: our website and address, etc
o Engaging pictures and graphics.
• The rest of the tone and manner are the same as the sermon series graphic.
The flyer will be 11X14, like a postcard size.

Target Market(s)

Young families who are spiritually curious but not committed church attenders.

Colors

Designer to choose colors to be used in the design.

Requirements
Nice to have
• A modern and professional looking design.
Should not have
• Anything offensive or not family friendly.

```html
<!DOCTYPE html>
<html lang="en">
<head>
<meta charset="utf-8">
<title>Harbor Lanterns – Westbrook Commons Open Day</title>
<link href="https://fonts.googleapis.com/css2?family=Dancing+Script:wght@600;700&family=Alegreya:wght@400;700&family=Lato:wght@400;700&display=swap" rel="stylesheet">
<style>
  :root {
    --backdrop: #8e8e8e;
    --navy-deep: #0f2a63;
    --navy-mid: #1d4391;
    --royal: #1f5bb5;
    --royal-dark: #17479a;
    --orange: #f08a1c;
    --white: #ffffff;
    --ink-blue: #1f4f9e;
    --text-dark: #2b2b2b;
  }
  * { margin: 0; padding: 0; box-sizing: border-box; }
  html, body { width: 800px; height: 1200px; overflow: hidden; }
  body {
    background: var(--backdrop);
    position: relative;
    font-family: 'Alegreya', serif;
  }
  .card {
    position: absolute;
    left: 75px;
    width: 650px;
    box-shadow: 0 6px 18px rgba(0,0,0,0.45);
    overflow: hidden;
  }

  /* Front: series card */
  .series-card {
    top: 35px;
    height: 530px;
    background: radial-gradient(ellipse at 45% 40%, var(--navy-mid) 0%, var(--navy-deep) 75%);
  }
  .series-card .texture {
    position: absolute; inset: 0;
    background: linear-gradient(135deg, rgba(255,255,255,0.05) 0%, rgba(255,255,255,0) 40%, rgba(255,255,255,0.06) 70%, rgba(0,0,0,0.1) 100%);
  }
  .series-card .frame {
    position: absolute;
    inset: 22px;
    border: 2px solid rgba(255,255,255,0.85);
  }
  .series-title {
    position: absolute; top: 62px; width: 100%;
    text-align: center;
    font-family: 'Dancing Script', cursive;
    font-weight: 700;
    font-size: 76px;
    color: var(--white);
  }
  .series-subtitle {
    position: absolute; top: 178px; width: 100%;
    text-align: center;
    font-weight: 700;
    font-size: 36px;
    color: var(--orange);
  }
  .church-name {
    position: absolute; width: 100%;
    text-align: center;
    display: flex; flex-direction: column; align-items: center; gap: 10px;
    font-family: 'Alegreya', serif;
  }
  .series-card .church-name { top: 262px; color: var(--white); font-size: 19px; }
  .church-name .mark {
    width: 70px; height: 70px; border-radius: 50%;
    border: 4px solid var(--orange);
  }
  .series-mission {
    position: absolute; top: 430px; width: 100%;
    text-align: center;
    font-size: 27px;
    color: var(--white);
  }

  /* Back: event card */
  .event-card {
    top: 605px;
    height: 560px;
    background: var(--white);
  }
  .event-card .band { position: absolute; left: 0; top: 0; }
  .event-title {
    position: absolute; top: 22px; width: 100%;
    text-align: center;
    font-family: 'Dancing Script', cursive;
    font-weight: 700;
    font-size: 44px;
    color: var(--white);
  }
  .event-date {
    position: absolute; top: 78px; width: 100%;
    text-align: center;
    font-size: 32px;
    color: var(--white);
  }
  .features {
    position: absolute; left: 150px; top: 135px;
    width: 350px; height: 160px;
    background: var(--white);
    border: 2px solid var(--royal-dark);
    border-radius: 8px;
    text-align: center;
    padding-top: 6px;
  }
  .features h2 {
    font-family: 'Dancing Script', cursive;
    font-weight: 700;
    font-size: 30px;
    color: var(--ink-blue);
    line-height: 1.1;
  }
  .features ul { list-style: none; margin-top: 4px; }
  .features li {
    font-size: 15px; line-height: 1.4;
    color: var(--text-dark);
  }
  .features li::before { content: "✓ "; color: var(--text-dark); }
  .event-card .church-name { top: 345px; color: var(--text-dark); font-size: 14px; gap: 6px; }
  .event-card .church-name .mark { width: 52px; height: 52px; border-width: 3px; }
  .contact {
    position: absolute; width: 100%;
    display: flex; justify-content: center; align-items: center; gap: 8px;
    font-family: 'Lato', sans-serif;
    font-size: 14px;
    color: var(--ink-blue);
  }
  .contact-address { top: 448px; }
  .contact-row { top: 494px; gap: 44px; }
  .contact-item { display: flex; align-items: center; gap: 7px; }
  .icon { width: 16px; height: 16px; fill: var(--ink-blue); }
</style>
</head>
<body>

<section class="card series-card">
  <div class="texture" role="img" aria-label="Faint geometric facet pattern across the deep blue background"></div>
  <div class="frame"></div>
  <h1 class="series-title">Harbor Lanterns</h1>
  <p class="series-subtitle">What’s keeping you from God?</p>
  <div class="church-name"><span class="mark"></span><span>Alder Grove Family Church</span></div>
  <p class="series-mission">Connecting Young Families to Christ</p>
</section>

<section class="card event-card">
  <svg class="band" width="650" height="400" viewBox="0 0 650 400">
    <path d="M0 0 H650 V396 Q325 276 0 396 Z" fill="var(--orange)"/>
    <path d="M0 0 H650 V386 Q325 266 0 386 Z" fill="var(--white)"/>
    <path d="M0 0 H650 V374 Q325 254 0 374 Z" fill="var(--royal)"/>
  </svg>
  <h1 class="event-title">Westbrook Commons Open Day</h1>
  <p class="event-date">Date: Sept 23rd @ 10:30</p>
  <div class="features">
    <h2>Features of the event:</h2>
    <ul>
      <li>Free lunch</li>
      <li>Children’s program</li>
      <li>Bouncy Castle</li>
      <li>Start of the “Harbor Lanterns” messages.</li>
      <li>Sample of topics</li>
    </ul>
  </div>
  <div class="church-name"><span class="mark"></span><span>Alder Grove Family Church</span></div>
  <p class="contact contact-address">
    <svg class="icon" viewBox="0 0 16 16"><path d="M8 0a5.5 5.5 0 0 0-5.5 5.5C2.5 10 8 16 8 16s5.5-6 5.5-10.5A5.5 5.5 0 0 0 8 0zm0 7.8a2.3 2.3 0 1 1 0-4.6 2.3 2.3 0 0 1 0 4.6z"/></svg>
    <span>1185 Maple Ridge Road, Oakdale, ON N0B 2K0 Canada</span>
  </p>
  <div class="contact contact-row">
    <span class="contact-item">
      <svg class="icon" viewBox="0 0 16 16"><path d="M3.6 1 6 3.9 4.7 5.6a9 9 0 0 0 5.7 5.7L12.1 10 15 12.4 13.5 15C6.8 14.6 1.4 9.2 1 2.5z"/></svg>
      555.014.2730
    </span>
    <span class="contact-item">
      <svg class="icon" viewBox="0 0 16 16"><path d="M1 3h14v10H1z M1.5 3.5 8 9l6.5-5.5" fill="none" stroke="var(--ink-blue)" stroke-width="1.5"/></svg>
      hello@aldergrovechurch.ca
    </span>
    <span class="contact-item">
      <svg class="icon" viewBox="0 0 16 16"><circle cx="8" cy="8" r="6.5" fill="none" stroke="var(--ink-blue)" stroke-width="1.4"/><path d="M1.5 8h13M8 1.5c-3 3.5-3 9.5 0 13M8 1.5c3 3.5 3 9.5 0 13" fill="none" stroke="var(--ink-blue)" stroke-width="1.2"/></svg>
      www.aldergrovechurch.ca
    </span>
  </div>
</section>

</body>
</html>
```